Borrowdale Equity Business Card

Looking for a design for our business cards. Need to look corporate and outstanding. I have enclosed our logos for the company. Borrowdale equity is an investment firm for high level clients looking for advisory in their investments. White background or black is good. We will like to double sided options maybe at the back with just the logo of the firm.

Example of the info for the business card:

Marcus Heller
Managing Director

Panama Phone +507 391 4786
Switzerland Phone +41 43 917 2648
test@borrowdale-equity-example.com
www.borrowdale-equity-example.com

Industry/Entity Type

Investment

```html
<!DOCTYPE html>
<html lang="en">
<head>
<meta charset="utf-8">
<title>Borrowdale Equity – Business Card</title>
<link href="https://fonts.googleapis.com/css2?family=Cinzel:wght@400;600&family=Open+Sans:wght@400;600&display=swap" rel="stylesheet">
<style>
  :root {
    --page-bg: #ecebe8;
    --card-white: #ffffff;
    --brand-blue: #1d4aa0;
    --brand-blue-deep: #123a86;
    --brand-blue-light: #2a5cb8;
    --brand-gold: #c9a52a;
    --text-dark: #2c3550;
    --text-grey: #6b6f78;
  }
  * { box-sizing: border-box; margin: 0; padding: 0; }
  html, body {
    width: 1171px; height: 1200px; overflow: hidden;
    background: var(--page-bg);
  }
  .canvas {
    position: relative; width: 1171px; height: 1200px;
  }
  .card {
    position: absolute; left: 155px; width: 860px; height: 490px;
    border-radius: 6px; overflow: hidden;
    box-shadow: 0 10px 30px rgba(0,0,0,.18);
  }
  .card--front { top: 75px; background: var(--card-white); }
  .card--back {
    top: 635px;
    background: linear-gradient(160deg, var(--brand-blue-light) 0%, var(--brand-blue) 45%, var(--brand-blue-deep) 100%);
  }

  /* Wordmark */
  .wordmark { position: absolute; display: flex; align-items: center; gap: 22px; }
  .wordmark__square { width: 44px; height: 44px; background: var(--brand-gold); }
  .wordmark__name {
    font-family: "Cinzel", serif; font-weight: 600; line-height: 1;
  }
  .wordmark__line1 { display: block; letter-spacing: 2px; }
  .wordmark__line2 { display: block; letter-spacing: 14px; margin-top: 8px; }

  .card--front .wordmark { left: 70px; top: 90px; }
  .card--front .wordmark__name { color: var(--brand-blue); }
  .card--front .wordmark__line1 { font-size: 46px; }
  .card--front .wordmark__line2 { font-size: 20px; }

  /* Holder */
  .holder {
    position: absolute; right: 60px; top: 70px; text-align: right;
    font-family: "Cinzel", serif;
  }
  .holder__name { font-size: 30px; color: var(--brand-blue); font-weight: 400; letter-spacing: 1px; }
  .holder__title { font-size: 14px; color: var(--text-grey); letter-spacing: 2px; margin-top: 4px; }

  /* Contacts */
  .contact-tab {
    position: absolute; left: 40px; top: 238px; width: 62px; height: 252px;
    background: var(--brand-blue); border-radius: 10px 10px 0 0;
  }
  .contact-list {
    position: absolute; left: 40px; top: 252px; list-style: none;
    font-family: "Open Sans", sans-serif; font-size: 17px; color: var(--text-dark);
  }
  .contact-list li { display: flex; align-items: flex-start; height: 46px; }
  .contact-list li.contact--address { height: 70px; }
  .contact__icon { width: 62px; display: flex; justify-content: center; padding-top: 1px; }
  .contact__icon svg { width: 24px; height: 24px; fill: #fff; }
  .contact__text { padding-left: 18px; line-height: 24px; }

  .edge-band {
    position: absolute; left: 0; right: 0; bottom: 0; height: 16px;
    background: var(--brand-blue);
  }
  .edge-band__accent {
    position: absolute; right: 0; top: 0; width: 110px; height: 100%;
    background: var(--brand-gold);
  }

  /* Back */
  .card--back .wordmark { left: 150px; top: 150px; }
  .card--back .wordmark__name { color: #fff; }
  .card--back .wordmark__line1 { font-size: 64px; }
  .card--back .wordmark__line2 { font-size: 26px; letter-spacing: 20px; margin-top: 10px; }
  .card--back .wordmark__square { width: 56px; height: 56px; }
  .web-address {
    position: absolute; left: 228px; top: 330px;
    font-family: "Cinzel", serif; font-size: 20px; letter-spacing: 3px; color: #fff;
  }
</style>
</head>
<body>
<div class="canvas">

  <section class="card card--front" aria-label="Business card front">
    <div class="wordmark">
      <span class="wordmark__square"></span>
      <span class="wordmark__name">
        <span class="wordmark__line1">BORROWDALE</span>
        <span class="wordmark__line2">EQUITY</span>
      </span>
    </div>

    <div class="holder">
      <div class="holder__name">YOUR NAME</div>
      <div class="holder__title">DESIGNATION</div>
    </div>

    <div class="contact-tab"></div>
    <ul class="contact-list">
      <li>
        <span class="contact__icon"><svg viewBox="0 0 24 24"><path d="M6.6 10.8a15.1 15.1 0 0 0 6.6 6.6l2.2-2.2a1 1 0 0 1 1-.25 11.4 11.4 0 0 0 3.6.57 1 1 0 0 1 1 1V20a1 1 0 0 1-1 1A17 17 0 0 1 3 4a1 1 0 0 1 1-1h3.5a1 1 0 0 1 1 1c0 1.25.2 2.45.57 3.57a1 1 0 0 1-.25 1z"/></svg></span>
        <span class="contact__text">+507 391 4786 (Panama)</span>
      </li>
      <li>
        <span class="contact__icon"><svg viewBox="0 0 24 24"><path d="M6.6 10.8a15.1 15.1 0 0 0 6.6 6.6l2.2-2.2a1 1 0 0 1 1-.25 11.4 11.4 0 0 0 3.6.57 1 1 0 0 1 1 1V20a1 1 0 0 1-1 1A17 17 0 0 1 3 4a1 1 0 0 1 1-1h3.5a1 1 0 0 1 1 1c0 1.25.2 2.45.57 3.57a1 1 0 0 1-.25 1z"/></svg></span>
        <span class="contact__text">+41 43 917 2648 (Switzerland)</span>
      </li>
      <li>
        <span class="contact__icon"><svg viewBox="0 0 24 24"><path d="M3 5h18v14H3z M3 5l9 7 9-7" fill="none" stroke="#fff" stroke-width="2" stroke-linejoin="round"/></svg></span>
        <span class="contact__text">test@borrowdale-equity-example.com</span>
      </li>
      <li class="contact--address">
        <span class="contact__icon"><svg viewBox="0 0 24 24"><path d="M12 2a7 7 0 0 0-7 7c0 5.2 7 13 7 13s7-7.8 7-13a7 7 0 0 0-7-7zm0 9.5A2.5 2.5 0 1 1 12 6.5a2.5 2.5 0 0 1 0 5z"/></svg></span>
        <span class="contact__text">57 Larkspur Road<br>Milbrook, Queensland 4712</span>
      </li>
    </ul>

    <div class="edge-band"><span class="edge-band__accent"></span></div>
  </section>

  <section class="card card--back" aria-label="Business card back">
    <div class="wordmark">
      <span class="wordmark__square"></span>
      <span class="wordmark__name">
        <span class="wordmark__line1">BORROWDALE</span>
        <span class="wordmark__line2">EQUITY</span>
      </span>
    </div>
    <div class="web-address">WWW.BORROWDALE-EQUITY-EXAMPLE.COM</div>
  </section>

</div>
</body>
</html>
```